Emergency Vehicle Installer and Security Firm Needs a Business Card

Our company "Corvalt" need a business card for our Emergency Vehicle Equipment Installation and Infrastructure Security Business. We are contract designers, manufacturers and installers for Emergency Vehicle Fleets. This includes installation of Emergency Lights, Sirens, Vehicle Graphics and Radio Communications. We also supply this products to an international market. We also do consultant, and installation of high level security access, alarm and surveillance equipment for medium to large size businesses.

The design should represent a level of trust in our professionalism and expertise. It should visually display our ongoing relationship with the emergency services, but not overtake our commitment to high level security options.

Target Market(s)

Emergency Services and Businesses requiring high level security

Industry/Entity Type

Business

Contact Information for Business Card

*note complete details will be given to the winning designer for revising. The name "Mark Pell will be used to fill in name".

Mark Pell
Managing Director
Corvalt NZ Limited
Phone: +64 027 604 91352
Email: mark.pell@corvalt-example.co.nz

Requirements
Must have
• Card must be in black. Using our logo on the top as supplied. Designers should try having the reverse side as a blurred image of police lights (red and blue) with our logo in greyscale in the centre (this is not particularly a requirement, but feel free to play around with this option).
Nice to have
• A card design that looks good when spot UV printed. A clean compact and graphic design. A grey scale feel on the front (excluding logo, but you can play around with that idea). Rounded smooth text.
Should not have
• Will update this section as designs come through - feel free to submit what you feel would look good.

```html
<!DOCTYPE html>
<html lang="en">
<head>
<meta charset="utf-8">
<title>Corvalt Business Card</title>
<link href="https://fonts.googleapis.com/css2?family=Roboto:wght@300;400;500;700;900&display=swap" rel="stylesheet">
<style>
  :root {
    --page: #ffffff;
    --card-black: #1f1f20;
    --accent-red: #e41e26;
    --band-red: #ec1c24;
    --text-white: #ffffff;
    --text-soft: #e6e6e6;
    --night-blue: #231c6e;
    --mid-violet: #4a1f5e;
    --deep-red: #7a0f2a;
  }
  * { margin: 0; padding: 0; box-sizing: border-box; }
  html, body { width: 1200px; height: 1200px; overflow: hidden; background: var(--page); }
  body { position: relative; font-family: 'Roboto', sans-serif; }

  .card {
    position: absolute;
    left: 227px;
    width: 775px;
    height: 443px;
    overflow: hidden;
    box-shadow: 0 10px 40px rgba(0,0,0,0.28);
  }
  .card--front { top: 136px; background: var(--card-black); }
  .card--back  { top: 621px; }

  .brand-name {
    position: absolute;
    font-family: 'Roboto', sans-serif;
    font-weight: 900;
    font-size: 68px;
    line-height: 1;
    letter-spacing: 1px;
    text-transform: uppercase;
    color: var(--text-white);
  }
  .card--front .brand-name { left: 33px; top: 192px; }

  .divider {
    position: absolute;
    left: 387px; top: 48px;
    width: 2px; height: 347px;
    background: var(--accent-red);
  }

  .person {
    position: absolute;
    right: 38px; top: 42px;
    text-align: right;
  }
  .person__name {
    font-size: 48px;
    font-weight: 300;
    line-height: 1;
    color: var(--text-white);
    text-transform: uppercase;
  }
  .person__name strong { font-weight: 700; }
  .person__title {
    margin-top: 6px;
    font-size: 19px;
    font-weight: 300;
    color: var(--accent-red);
    text-transform: uppercase;
    letter-spacing: 0.3px;
  }

  .contact {
    position: absolute;
    left: 436px; top: 304px;
    color: var(--text-soft);
    text-transform: uppercase;
  }
  .contact__company {
    margin-left: 40px;
    font-size: 18px;
    font-weight: 700;
    color: var(--text-white);
    line-height: 24px;
  }
  .contact__row {
    display: flex;
    align-items: center;
    margin-top: 7px;
    font-size: 18px;
    font-weight: 300;
    line-height: 24px;
    white-space: nowrap;
  }
  .contact__row--email { font-size: 16px; margin-top: 8px; letter-spacing: -0.2px; }
  .contact__icon { width: 26px; height: 20px; margin-right: 14px; flex: none; }

  .lights {
    position: absolute; inset: 0;
    background: linear-gradient(115deg, var(--night-blue) 0%, var(--mid-violet) 45%, var(--deep-red) 100%);
  }
  .band {
    position: absolute;
    left: 0; right: 0; top: 151px; height: 140px;
    background: var(--band-red);
  }
  .card--back .brand-name {
    left: 0; right: 0; top: 188px;
    text-align: center;
  }
</style>
</head>
<body>

<section class="card card--front" aria-label="Business card front">
  <div class="brand-name">Corvalt</div>
  <div class="divider"></div>

  <div class="person">
    <div class="person__name">Mark <strong>Pell</strong></div>
    <div class="person__title">Managing Director</div>
  </div>

  <div class="contact">
    <div class="contact__company">Corvalt NZ Limited</div>
    <div class="contact__row">
      <svg class="contact__icon" viewBox="0 0 26 20" aria-hidden="true">
        <path fill="#ffffff" d="M6 1.5l3 0 1.6 4.2-2.1 1.6c1 2.3 2.8 4.1 5.1 5.1l1.6-2.1 4.2 1.6 0 3c0 1.1-.9 2-2 2C9.5 16.9 4 11.4 4 3.5c0-1.1.9-2 2-2z"/>
      </svg>
      <span>+64 027 604 91352</span>
    </div>
    <div class="contact__row contact__row--email">
      <svg class="contact__icon" viewBox="0 0 26 20" aria-hidden="true">
        <rect x="1" y="2" width="24" height="16" fill="#ffffff"/>
        <path d="M1 2l12 9 12-9M1 18l9-8M25 18l-9-8" fill="none" stroke="#1f1f20" stroke-width="1.5"/>
      </svg>
      <span>mark.pell@corvalt-example.co.nz</span>
    </div>
  </div>
</section>

<section class="card card--back" aria-label="Business card back">
  <div class="lights" role="img" aria-label="Blurred photograph of red and blue emergency vehicle lights"></div>
  <div class="band"></div>
  <div class="brand-name">Corvalt</div>
</section>

</body>
</html>
```